Audio Visual & Broadcast Installing Company needs a Web Site Design

We need a website design for our company Corvane Ltd. We are a small company that does Audio Visual and broadcast installations. We are looking to expand our business and need a professional web presence. All work completed by us is done to a very high standard and it’s this attention to detail that sets us apart from our competitors. Our projects include doing fibre optics at major sporting events; installing and commissioning bespoke control systems on super yachts and installing the latest systems in luxury homes.

We provide the following services:
System design
On-site installation
Rack building
Pre-fabricated cable looms
Fibre optic cabling

We would like a website that gives details of our services and provides contact information. Our customers are other businesses and our website needs to reflect this. The flyer attached will be used to promote the company and we would like the website to follow this theme. Please use the colours from our logo, as the colour scheme. We know that our colours are bright and we don’t want them to overwhelm the site. With our website we want to communicate that we are professional and provide a quality service.
NB UPDATE: please use stock images for any graphical elements.

The following 3 sites belong to some of our competitors. The first 2, we DON'T like because they don't project a professional feeling. The last one, 'vellumspire', is better as it provides the required information in a clear, simple form.

http://www.plomquist-example.com/

http://www.heronfieldlinkworks-example.com/

http://www.vellumspire-example.com/

We really like the following site, it feels professional and high end without too many flashy graphics. We want something that is fast to load but still shows the high end quality of our work.

http://osmerdalegroup-example.com/

Pages/Sections

Home
On site installation
Rack building and cable looms
Fibre optics
Portfolio (this will be limited to start with but must be easy to expand and add new projects)
Updates

Target Market(s)

Businesses operating in the following areas:
Audio Vision, Broadcasting, Home Automation, Events

Industry/Entity Type

Broadcasting

Coding

Coded - Design and coding required

Number of Pages Required

4 page

Font styles to use
Other font styles liked:
• similar to attached flyer

Requirements
Must have
• The same theme as the 'flyer1' attachment.

```html
<!DOCTYPE html>
<html lang="en">
<head>
<meta charset="utf-8">
<title>Corvane Ltd — Audio Visual &amp; Broadcast Installations</title>
<link rel="stylesheet" href="https://fonts.googleapis.com/css2?family=Montserrat:wght@300;400;500;600;700&display=swap">
<style>
:root{
  --dark:#2e2e30;
  --ink:#2b2b2b;
  --white:#ffffff;
  --red:#d8154a;
  --blue:#1f80ea;
  --yellow:#f2b705;
  --font:'Montserrat', Arial, sans-serif;
}
*{box-sizing:border-box;margin:0;padding:0}
html,body{width:1200px;height:3990px;overflow:hidden;background:var(--dark)}
body{font-family:var(--font);color:var(--white)}
.page{position:relative;width:1200px;height:3990px;overflow:hidden;background:var(--dark)}
.abs{position:absolute}

/* header */
.site-header{position:absolute;top:0;left:0;width:1200px;height:100px;background:var(--white);z-index:5}
.brand{position:absolute;left:52px;top:34px;display:flex;align-items:center;gap:10px}
.brand-mark{width:26px;height:26px;background:var(--red)}
.brand-name{font-weight:700;font-size:26px;color:var(--ink)}
.main-nav{position:absolute;right:50px;top:40px;display:flex;gap:24px;font-size:15px;font-weight:500;color:var(--ink)}

/* hero */
.hero{position:absolute;top:100px;left:0;width:1200px;height:660px}
.hero-art{position:absolute;top:0;left:0}
.hero-text{position:absolute;top:190px;left:0;width:1200px;text-align:center;color:var(--ink)}
.hero-text .strong{font-weight:700;font-size:40px;letter-spacing:1px;line-height:50px}
.hero-text .light{font-weight:400;font-size:36px;letter-spacing:1px;line-height:44px}
.btn{display:inline-block;background:var(--ink);color:var(--white);font-weight:600;font-size:16px;letter-spacing:1px;padding:14px 40px}
.hero .btn{margin-top:22px}

/* headings */
.heading{font-weight:500;font-size:52px}
.heading-line{width:150px;height:2px;background:currentColor;margin-top:12px}
.copy{font-size:15px;line-height:30px;color:var(--white)}

/* about */
.about-photo{left:0;top:895px;width:360px;height:215px}
.about-claim{left:52px;top:1130px;width:520px;color:var(--yellow);font-size:34px;line-height:44px;font-weight:500}
.about-claim-strong{left:52px;top:1265px;color:var(--yellow);font-size:40px;font-weight:700}
.about-heading{left:645px;top:878px;color:var(--yellow)}
.about-copy{left:645px;top:985px;width:510px}

/* on-site */
.onsite-wave{left:0;top:1330px;width:1200px;height:900px}
.onsite-text{left:0;top:1590px;width:1200px;text-align:center;color:var(--ink)}
.onsite-text .heading-line{margin:12px auto 0}
.onsite-text .copy{color:#444;width:840px;margin:38px auto 0;font-size:14px;line-height:30px}
.onsite-text .btn{margin-top:28px}

/* services */
.services-intro{left:645px;top:2245px;width:510px}
.connect-title{left:52px;top:2370px;width:520px;color:var(--yellow);font-size:36px;line-height:46px;font-weight:700}
.connect-copy{left:52px;top:2508px;width:510px}
.services-heading{left:645px;top:2372px;color:var(--yellow)}
.service-list{left:645px;top:2475px;list-style:none}
.service-list li{display:flex;align-items:center;gap:28px;height:62px;font-size:15px}
.service-list svg{width:42px;height:42px}

/* portfolio */
.portfolio-wave{left:0;top:2760px;width:1200px;height:900px}
.portfolio-heading{left:0;top:2925px;width:1200px;text-align:center;color:var(--ink);font-size:48px;font-weight:600}
.portfolio-heading .heading-line{margin:10px auto 0;width:130px;background:var(--ink)}
.project{top:3080px;width:335px;height:290px}
.arrow{top:3205px;width:24px;height:40px}

/* footer */
.footer-brand{left:150px;top:3625px;display:flex;align-items:center;gap:12px}
.footer-brand .brand-mark{width:34px;height:34px}
.footer-brand .brand-name{color:var(--white);font-size:32px}
.social{left:150px;top:3790px;display:flex;gap:12px}
.social span{width:34px;height:34px;border-radius:50%;background:var(--white)}
.footer-col h4{color:var(--yellow);font-size:20px;font-weight:600;margin-bottom:16px}
.footer-col p{font-size:15px;line-height:30px}
.contact-col{left:465px;top:3615px;width:300px}
.newsletter-col{left:800px;top:3615px;width:360px}
.newsletter-col p{line-height:22px}
.newsletter-form{display:flex;margin-top:14px}
.newsletter-form .field{width:250px;height:46px;border:2px solid var(--yellow);font-size:15px;padding:12px;color:var(--white)}
.newsletter-form .submit{width:110px;height:46px;background:var(--yellow);color:var(--ink);font-weight:600;font-size:16px;display:flex;align-items:center;justify-content:center}
.footer-rule{left:0;top:3905px;width:1200px;height:1px;background:#555}
.copyright{left:0;top:3935px;width:1200px;text-align:center;font-size:15px;font-weight:500}
</style>
</head>
<body>
<div class="page">

  <header class="site-header">
    <div class="brand"><span class="brand-mark"></span><span class="brand-name">Corvane Ltd</span></div>
    <nav class="main-nav">
      <span>Home</span><span>About Us</span><span>On-Site Installation</span><span>Services</span><span>Fibre Optics</span><span>Portfolio</span><span>Contact Us</span>
    </nav>
  </header>

  <section class="hero">
    <svg class="hero-art" width="1200" height="660" viewBox="0 0 1200 660" role="img" aria-label="Photo of audio cables plugged into a mixing desk">
      <defs>
        <linearGradient id="heroFill" x1="0" y1="0" x2="0" y2="1">
          <stop offset="0" stop-color="#f4f3f1"/>
          <stop offset=".35" stop-color="#e3ddd3"/>
          <stop offset=".7" stop-color="#cfc6b8"/>
          <stop offset="1" stop-color="#b9b2a8"/>
        </linearGradient>
        <radialGradient id="heroGlow" cx=".5" cy=".42" r=".55">
          <stop offset="0" stop-color="#fbf8f2" stop-opacity=".95"/>
          <stop offset=".6" stop-color="#e9dfcc" stop-opacity=".35"/>
          <stop offset="1" stop-color="#8f8578" stop-opacity=".3"/>
        </radialGradient>
      </defs>
      <rect width="1200" height="660" fill="url(#heroFill)"/>
      <rect width="1200" height="660" fill="url(#heroGlow)"/>
      <path d="M0 430 C250 560 600 600 1200 500 L1200 660 L0 660Z" fill="var(--white)"/>
      <path d="M0 470 C250 610 600 640 1200 520 L1200 660 L0 660Z" fill="var(--red)"/>
      <path d="M0 540 C260 650 650 670 1200 540 L1200 660 L0 660Z" fill="var(--dark)"/>
    </svg>
    <div class="hero-text">
      <div class="strong">Broadcasting Ashgrove Open</div>
      <div class="light">Was Equally Thrilling As</div>
      <div class="strong">Playing Ashgrove Open</div>
      <span class="btn">EXPLORE</span>
    </div>
  </section>

  <section class="about">
    <svg class="abs about-photo" viewBox="0 0 360 215" role="img" aria-label="Photo of HDMI cable connectors">
      <defs>
        <linearGradient id="aboutFill" x1="0" y1=".5" x2="1" y2=".5">
          <stop offset="0" stop-color="#5a1722"/>
          <stop offset=".45" stop-color="#8c2a35"/>
          <stop offset=".75" stop-color="#c9b79a"/>
          <stop offset="1" stop-color="#e6dcc6"/>
        </linearGradient>
      </defs>
      <rect width="360" height="215" fill="url(#aboutFill)"/>
    </svg>
    <p class="abs about-claim">Lorem ipsum dolor sit amet, consectetur adipiscing elit, sed do eiusmod tempor.</p>
    <p class="abs about-claim-strong">And We Delivered</p>
    <div class="abs about-heading"><h2 class="heading">About Us</h2><div class="heading-line"></div></div>
    <p class="abs copy about-copy">Lorem ipsum dolor sit amet, consectetur adipiscing elit, sed do eiusmod tempor incididunt ut labore et dolore magna aliqua. Ut enim ad minim veniam, quis nostrud exercitation ullamco laboris nisi ut aliquip ex ea commodo consequat. Duis aute irure dolor in reprehenderit in voluptate velit esse cillum dolore eu fugiat nulla pariatur.<br>Ut enim ad minim veniam, quis nostrud exercitation ullamco laboris nisi ut aliquip ex ea commodo consequat. Duis aute irure dolor in reprehenderit.</p>
  </section>

  <section class="onsite">
    <svg class="abs onsite-wave" viewBox="0 0 1200 900" role="img" aria-label="Photo of a hi-fi speaker and amplifier setup">
      <defs>
        <linearGradient id="onsiteFill" x1="0" y1="0" x2="1" y2="0">
          <stop offset="0" stop-color="#e4e7eb"/>
          <stop offset=".5" stop-color="#f7f8fa"/>
          <stop offset="1" stop-color="#e4e7eb"/>
        </linearGradient>
      </defs>
      <path d="M560 110 C800 40 1050 20 1200 40 L1200 200 C1000 120 800 100 560 110Z" fill="var(--blue)"/>
      <path d="M0 130 C300 50 800 50 1200 120 L1200 640 C900 760 500 790 0 640Z" fill="url(#onsiteFill)"/>
      <path d="M0 640 C400 790 900 760 1200 640 L1200 700 C900 830 400 860 0 710Z" fill="var(--red)"/>
    </svg>
    <div class="abs onsite-text">
      <h2 class="heading">On-Site Installation</h2>
      <div class="heading-line"></div>
      <p class="copy">Lorem ipsum dolor sit amet, consectetur adipiscing elit, sed do eiusmod tempor incididunt ut labore et dolore magna aliqua. Ut enim ad minim veniam, quis nostrud exercitation ullamco laboris nisi ut aliquip ex ea commodo consequat. Duis aute irure dolor in reprehenderit in voluptate velit esse cillum dolore eu fugiat nulla pariatur.<br>Quis nostrud exercitation ullamco laboris nisi ut aliquip ex ea commodo consequat. Duis aute irure dolor in reprehenderit in voluptate velit esse cillum dolore eu fugiat nulla pariatur.</p>
      <span class="btn">KNOW MORE</span>
    </div>
  </section>

  <section class="services">
    <p class="abs copy services-intro">labore et dolore magna aliqua. Ut enim ad minim veniam, quis nostrud exercitation ullamco laboris nisi ut aliquip ex ea commodo consequat. Duis aute irure dolor in reprehenderit in voluptate velit esse cillum dolore eu fugiat nulla pariatur.</p>
    <h3 class="abs connect-title">Making The Connections That Digital Innovation Demands</h3>
    <p class="abs copy connect-copy">Lorem ipsum dolor sit amet, consectetur adipiscing elit, sed do eiusmod tempor incididunt ut labore et dolore magna aliqua. Ut enim ad minim veniam, quis nostrud exercitation.</p>
    <div class="abs services-heading"><h2 class="heading">Services</h2></div>
    <ul class="abs service-list">
      <li><svg viewBox="0 0 42 42" fill="none" stroke="#fff" stroke-width="2"><circle cx="21" cy="21" r="4"/><path d="M13 13a11 11 0 0 0 0 16M29 13a11 11 0 0 1 0 16M8 8a18 18 0 0 0 0 26M34 8a18 18 0 0 1 0 26"/></svg>Broadcast/ AV System Design</li>
      <li><svg viewBox="0 0 42 42" fill="none" stroke="#fff" stroke-width="2"><path d="M21 6v20M13 18l8 8 8-8M7 28v8h28v-8"/></svg>On-site Installation</li>
      <li><svg viewBox="0 0 42 42" fill="none" stroke="#fff" stroke-width="2"><rect x="9" y="6" width="24" height="30"/><path d="M9 16h24M9 26h24"/></svg>Rack Building</li>
      <li><svg viewBox="0 0 42 42" fill="none" stroke="#fff" stroke-width="2"><path d="M16 6v8M24 6v8M12 14h16v8a8 8 0 0 1-16 0zM20 30v8"/></svg>Pre-fabricated Cable Looms</li>
      <li><svg viewBox="0 0 42 42" fill="none" stroke="#fff" stroke-width="2"><path d="M6 30c8 0 8-14 16-14s8 14 16 14M6 36h10"/></svg>Fibre Optic Cabling</li>
    </ul>
  </section>

  <section class="portfolio">
    <svg class="abs portfolio-wave" viewBox="0 0 1200 900">
      <path d="M560 110 C800 40 1050 20 1200 40 L1200 200 C1000 120 800 100 560 110Z" fill="var(--blue)"/>
      <path d="M0 130 C300 50 800 50 1200 120 L1200 660 C900 770 500 800 0 660Z" fill="var(--white)"/>
      <path d="M0 660 C400 800 900 770 1200 660 L1200 720 C900 840 400 870 0 730Z" fill="var(--red)"/>
    </svg>
    <div class="abs portfolio-heading">Portfolio<div class="heading-line"></div></div>
    <svg class="abs arrow" style="left:6px" viewBox="0 0 24 40"><path d="M18 6L6 20l12 14" fill="none" stroke="var(--ink)" stroke-width="3"/></svg>
    <svg class="abs project" style="left:55px" viewBox="0 0 335 290" role="img" aria-label="Project photo: colourful cables on a mixing console">
      <defs><linearGradient id="p1" x1="0" y1="0" x2="0" y2="1"><stop offset="0" stop-color="#e07bb0"/><stop offset=".6" stop-color="#d9a24a"/><stop offset="1" stop-color="#8e9aa6"/></linearGradient></defs>
      <rect width="335" height="290" fill="url(#p1)"/></svg>
    <svg class="abs project" style="left:432px" viewBox="0 0 335 290" role="img" aria-label="Project photo: DJ turntable under blue light">
      <defs><radialGradient id="p2" cx=".5" cy=".55" r=".6"><stop offset="0" stop-color="#6c7ce0"/><stop offset="1" stop-color="#1c2560"/></radialGradient></defs>
      <rect width="335" height="290" fill="url(#p2)"/></svg>
    <svg class="abs project" style="left:810px" viewBox="0 0 335 290" role="img" aria-label="Project photo: audio mixer with patch leads">
      <defs><linearGradient id="p3" x1="0" y1="0" x2="0" y2="1"><stop offset="0" stop-color="#9fb6b3"/><stop offset=".45" stop-color="#4a4646"/><stop offset="1" stop-color="#222"/></linearGradient></defs>
      <rect width="335" height="290" fill="url(#p3)"/></svg>
    <svg class="abs arrow" style="left:1166px" viewBox="0 0 24 40"><path d="M6 6l12 14-12 14" fill="none" stroke="var(--ink)" stroke-width="3"/></svg>
  </section>

  <footer class="site-footer">
    <div class="abs footer-brand"><span class="brand-mark"></span><span class="brand-name">Corvane Ltd</span></div>
    <div class="abs social"><span></span><span></span><span></span><span></span><span></span><span></span></div>
    <div class="abs footer-col contact-col">
      <h4>Contact</h4>
      <p>123 Street, Landmark,<br>Country 123456.<br>Phone:01234 123 4567<br>Email:info@corvane-example.com</p>
    </div>
    <div class="abs footer-col newsletter-col">
      <h4>Newsletter</h4>
      <p>Enter your email address to get the latest University news, special events and student activities delivered.</p>
      <div class="newsletter-form"><span class="field">Your Email id</span><span class="submit">Subscribe</span></div>
    </div>
    <div class="abs footer-rule"></div>
    <p class="abs copyright">© 2017 All Rights Reserved | Privacy Policy</p>
  </footer>

</div>
</body>
</html>
```